Can you make a cool and versatile Talvern Ridge Powerpoint template?
See www.talvernridge.co.uk and http://www.linkedin.com/company/talvern-ridge-ltd/ (on the right) to see how the logos are currently used - with interchangeably white and black backgrounds.
Target Market(s)
Marketing managers, product managers in HR technology, HR consultants
Industry/Entity Type
It Company
Font styles to use
Sans Serif
Requirements
Must have
- Master slide design, fonts, color theme, etc. Ideally two variations - one with white background (using colorful logo), one with a darker background (using black/white logo).

```html
<!DOCTYPE html>
<html lang="en">
<head>
<meta charset="utf-8">
<title>Talvern Ridge – Bullet Slide Template</title>
<link rel="stylesheet" href="https://fonts.googleapis.com/css2?family=Graduate&family=Cinzel:wght@400;500&family=PT+Sans:wght@400&display=swap">
<style>
  :root {
    --brand-blue: #29a9e1;
    --charcoal: #333335;
    --rule-dark: #3a3a3c;
    --paper-light: #f1f1f1;
    --paper-mid: #dcdcdc;
    --white: #ffffff;
    --ink: #1e1e1e;
  }
  * { margin: 0; padding: 0; box-sizing: border-box; }
  html, body {
    width: 1200px; height: 900px; overflow: hidden;
    background: var(--white);
    font-family: "PT Sans", Arial, sans-serif;
  }
  .canvas { position: relative; width: 1200px; height: 900px; }

  .corner-mark {
    position: absolute; left: 17px; top: 8px; width: 141px; height: 140px;
    background: var(--brand-blue);
    display: flex; align-items: center; justify-content: center;
    color: var(--white); font-family: "PT Sans", Arial, sans-serif;
    font-size: 17px; text-align: center; line-height: 1.2;
  }

  .slide {
    position: absolute; left: 23px; top: 165px; width: 1154px; height: 650px;
    background: radial-gradient(ellipse at 60% 45%, var(--paper-light), var(--paper-mid) 95%);
    overflow: hidden;
  }
  .slide-decor { position: absolute; left: 0; top: 0; }
  .slide-number {
    position: absolute; right: 28px; top: 32px;
    font-family: "Graduate", "Arial Black", sans-serif;
    color: var(--white); font-size: 24px;
    -webkit-text-stroke: 1.5px var(--white);
  }

  .bullet-list { position: absolute; left: 107px; top: 92px; }
  .main-bullet {
    display: flex; align-items: center; gap: 16px;
    font-family: "Graduate", "Arial Black", sans-serif;
    font-size: 48px; font-weight: 400; color: var(--brand-blue);
    -webkit-text-stroke: 2px var(--brand-blue);
  }
  .main-bullet-text { display: inline-block; transform: scaleX(0.86); transform-origin: left center; }
  .sub-bullets { list-style: none; margin: 4px 0 0 92px; }
  .sub-bullet {
    display: flex; align-items: center; gap: 12px;
    font-family: "Cinzel", Georgia, serif; font-weight: 500;
    font-size: 24px; color: var(--ink); height: 57px;
  }

  .title-bar {
    position: absolute; left: 16px; top: 493px; width: 1122px; height: 144px;
    background: var(--charcoal);
  }
  .slide-title {
    position: absolute; left: 26px; top: 14px;
    font-family: "Graduate", "Arial Black", sans-serif;
    font-size: 80px; line-height: 1; color: var(--brand-blue);
    font-weight: 400; white-space: nowrap;
    -webkit-text-stroke: 3.5px var(--brand-blue);
    transform: scaleX(0.85); transform-origin: left center;
  }
  .title-rule {
    position: absolute; left: 24px; top: 90px; width: 421px; height: 3px;
    background: var(--white);
  }
  .slide-subtitle {
    position: absolute; right: 676px; top: 103px;
    color: var(--white); font-size: 19.5px;
  }
  .contact {
    position: absolute; right: 173px; top: 57px; text-align: right;
    color: var(--white); font-size: 12px; line-height: 18px;
  }
  .brand-tile {
    position: absolute; right: 10px; top: 11px; width: 148px; height: 123px;
    background: var(--brand-blue);
    display: flex; align-items: center; justify-content: center;
    color: var(--white); font-size: 19px; text-align: center; line-height: 1.2;
  }
</style>
</head>
<body>
<main class="canvas">
  <div class="corner-mark">Talvern<br>Ridge</div>

  <section class="slide">
    <svg class="slide-decor" width="1154" height="650" aria-hidden="true">
      <line x1="62" y1="48" x2="1055" y2="48" stroke="var(--rule-dark)" stroke-width="4"/>
      <rect x="24" y="33" width="30" height="30" rx="6" transform="rotate(45 39 48)"
            fill="var(--white)" stroke="var(--rule-dark)" stroke-width="3.5"/>
      <circle cx="39" cy="48" r="9" fill="var(--brand-blue)"/>
      <polygon points="1037,15 1139,15 1139,115" fill="var(--brand-blue)"/>
    </svg>
    <span class="slide-number">03</span>

    <div class="bullet-list">
      <h2 class="main-bullet">
        <svg width="40" height="36" viewBox="0 0 40 36" aria-hidden="true">
          <polygon points="11,3 29,3 37,18 29,33 11,33 3,18" fill="none" stroke="var(--brand-blue)" stroke-width="5"/>
        </svg>
        <span class="main-bullet-text">MAIN BULLET</span>
      </h2>
      <ul class="sub-bullets">
        <li class="sub-bullet">
          <svg width="32" height="30" viewBox="0 0 32 30" aria-hidden="true">
            <polygon points="9,2 23,2 30,15 23,28 9,28 2,15" fill="var(--brand-blue)" stroke="var(--rule-dark)" stroke-width="3.5"/>
          </svg>SUB BULLET FORM</li>
        <li class="sub-bullet">
          <svg width="32" height="30" viewBox="0 0 32 30" aria-hidden="true">
            <polygon points="9,2 23,2 30,15 23,28 9,28 2,15" fill="var(--brand-blue)" stroke="var(--rule-dark)" stroke-width="3.5"/>
          </svg>SUB BULLET FORM</li>
        <li class="sub-bullet">
          <svg width="32" height="30" viewBox="0 0 32 30" aria-hidden="true">
            <polygon points="9,2 23,2 30,15 23,28 9,28 2,15" fill="var(--brand-blue)" stroke="var(--rule-dark)" stroke-width="3.5"/>
          </svg>SUB BULLET FORM</li>
      </ul>
    </div>

    <footer class="title-bar">
      <h1 class="slide-title">SLIDE TITLE</h1>
      <div class="title-rule"></div>
      <p class="slide-subtitle">BULLET FORM</p>
      <p class="contact">WWW.TALVERNRIDGE.CO.UK<br>HELLO@TALVERNRIDGE.CO.UK</p>
      <div class="brand-tile">Talvern<br>Ridge</div>
    </footer>
  </section>
</main>
</body>
</html>
```